Banner Ad Design Project

My online radio station features DJ sets periodically. The series is called "Deep Orbit" I need a versatile banner ad that I can add the DJ image to an area and then the date and time. I would assume we would agree the area where I can just add a layer via Photoshop with the DJ image and time info as I have more DJs. I will add one of my DJs images. You can crop as necessary. His airplay time is Friday 2pm set and 8pm set.

This is a DANCE radio station, so bright lights, lasers, etc will all be considered.

The banner size is 960X340

Target Market(s)

LGBT between 16-45

Industry/Entity Type

Radio

Requirements
Should not have
• although this is for LGBT, I do not want to see rainbow flags, headphones or other cheesy common themes

```html
<!DOCTYPE html>
<html lang="en">
<head>
<meta charset="utf-8">
<title>Deep Orbit – Friday 2PM &amp; 8PM</title>
<link rel="stylesheet" href="https://fonts.googleapis.com/css2?family=Orbitron:wght@500;700;800&display=swap">
<style>
  :root {
    --led-deep: #021238;
    --led-blue: #0a3fb8;
    --led-bright: #1c7fff;
    --led-cyan: #3fe6ff;
    --headline-yellow: #f4ef0a;
    --photo-slot: #5a5550;
    --photo-slot-dark: #2a2724;
  }
  html, body {
    margin: 0;
    padding: 0;
    overflow: hidden;
    background: #000;
  }
  .banner {
    position: relative;
    width: 1200px;
    height: 425px;
    overflow: hidden;
    font-family: "Orbitron", sans-serif;
    color: var(--headline-yellow);
  }
  .led-backdrop {
    position: absolute;
    inset: 0;
    background:
      radial-gradient(ellipse 30% 45% at 78% 18%, rgba(63,230,255,0.75), transparent 70%),
      radial-gradient(ellipse 35% 40% at 20% 75%, rgba(63,200,255,0.45), transparent 70%),
      radial-gradient(ellipse 60% 70% at 45% 55%, var(--led-bright), transparent 80%),
      linear-gradient(135deg, var(--led-blue) 0%, var(--led-deep) 55%, var(--led-blue) 100%);
  }
  .series-title {
    position: absolute;
    left: 10px;
    top: 2px;
    margin: 0;
    font-size: 118px;
    font-weight: 700;
    line-height: 1;
    letter-spacing: 2px;
    text-transform: uppercase;
    white-space: nowrap;
  }
  .featuring {
    position: absolute;
    left: 30px;
    top: 120px;
    margin: 0;
    font-size: 44px;
    font-weight: 700;
    line-height: 1;
    text-transform: uppercase;
  }
  .airtime {
    position: absolute;
    left: 30px;
    top: 348px;
    margin: 0;
    font-size: 46px;
    font-weight: 700;
    line-height: 1;
    letter-spacing: 1px;
    text-transform: uppercase;
    white-space: nowrap;
  }
  .dj-photo {
    position: absolute;
    left: 785px;
    top: 125px;
    width: 363px;
    height: 294px;
    background: linear-gradient(160deg, var(--photo-slot) 0%, var(--photo-slot-dark) 100%);
  }
</style>
</head>
<body>
  <div class="banner">
    <div class="led-backdrop" role="img" aria-label="Wall of glowing blue and cyan LED lights"></div>
    <h1 class="series-title">Deep Orbit</h1>
    <p class="featuring">Feat.</p>
    <div class="dj-photo" role="img" aria-label="Photo of the featured DJ in a cap and t-shirt"></div>
    <p class="airtime">Friday 2PM &amp; 8PM</p>
  </div>
</body>
</html>
```